Tovani Nightclub

Nightclub flyer., digital single sided, for FB and IG. I included samples of some previous flyers we've used. Sample Info:
TOVANI
FRIDAYS
FRI MAY 1 2020
DJ BRAVURA (club floor)
DJ ZOLT & DJ RAF (residents on the lounge floor)
4372 Birch Street Sacramento
www.tovanimurcott.com for list/VIP inquiries

Target Market(s)

Upscale top 40 crowd but want some cool and artsy like the examples included.

Font styles to use
Sans Serif

Requirements
Must have
• Tovani Logo
Nice to have
• Would be nice if the flyer can be incorporated later with DJ photos (sometimes we will add dj photos to instagram etc). Would like a big city type of feel.
Should not have
• Nothing too sexual.

```html
<!DOCTYPE html>
<html lang="en">
<head>
<meta charset="utf-8">
<title>Tovani Fridays – DJ Bravura</title>
<link rel="stylesheet" href="https://fonts.googleapis.com/css2?family=Jost:wght@300;400;600;700&display=swap">
<style>
  :root {
    --ink: #ffffff;
    --night-deep: #2a1470;
    --night-mid: #4a26a8;
    --night-violet: #6a2fc0;
    --night-magenta: #b13ab8;
    --night-indigo: #1c0f55;
  }
  * { margin: 0; padding: 0; box-sizing: border-box; }
  html, body { width: 1200px; height: 1200px; overflow: hidden; background: var(--night-indigo); }
  .flyer {
    position: relative;
    width: 1200px;
    height: 1200px;
    overflow: hidden;
    font-family: "Jost", "Futura", sans-serif;
    color: var(--ink);
  }
  .flyer__backdrop {
    position: absolute; inset: 0;
    background:
      radial-gradient(ellipse 60% 50% at 85% 90%, rgba(177,58,184,0.55), transparent 70%),
      radial-gradient(ellipse 40% 60% at 20% 40%, rgba(177,58,184,0.35), transparent 70%),
      linear-gradient(160deg, var(--night-mid) 0%, var(--night-deep) 45%, var(--night-violet) 100%);
  }
  .flyer__cityscape {
    position: absolute; left: 0; top: 0;
    width: 560px; height: 1200px;
    background: linear-gradient(90deg, rgba(120,40,190,0.55) 0%, rgba(150,50,200,0.35) 55%, transparent 100%);
  }
  .address {
    position: absolute; top: 30px; left: 0; right: 0;
    text-align: center;
    font-weight: 400; font-size: 30px; letter-spacing: 0.3em;
  }
  .headliner {
    position: absolute; top: 340px; left: 0; right: 0;
    text-align: center;
    font-weight: 400; font-size: 190px; line-height: 1; letter-spacing: 0.02em;
  }
  .residents {
    position: absolute; top: 585px; left: 0; right: 0;
    text-align: center;
    font-weight: 400; font-size: 106px; line-height: 1;
  }
  .date {
    position: absolute; top: 762px; left: 78px;
    font-weight: 700; font-size: 66px; line-height: 1; letter-spacing: 0.22em;
  }
  .venue-mark {
    position: absolute; top: 758px; left: 808px;
    display: flex; align-items: center; gap: 16px;
  }
  .venue-mark__dot {
    width: 70px; height: 70px; border-radius: 50%;
    background: var(--night-magenta);
  }
  .venue-mark__name {
    font-weight: 400; font-size: 44px; letter-spacing: 0.04em; color: var(--ink);
  }
  .website {
    position: absolute; top: 1124px; left: 0; right: 0;
    text-align: center;
    font-weight: 300; font-size: 40px; letter-spacing: 0.06em;
  }
</style>
</head>
<body>
  <main class="flyer">
    <div class="flyer__backdrop" role="img" aria-label="Starry violet night sky"></div>
    <div class="flyer__cityscape" role="img" aria-label="Glowing purple city skyscraper framework seen from below"></div>

    <p class="address">4372 BIRCH STREET SACRAMENTO</p>
    <h1 class="headliner">DJ BRAVURA</h1>
    <h2 class="residents">DJ ZOLT &amp; DJ RAF</h2>
    <p class="date">FRIDAY MAY 1</p>
    <div class="venue-mark">
      <span class="venue-mark__dot"></span>
      <span class="venue-mark__name">TOVANI</span>
    </div>
    <p class="website">WWW.TOVANIMURCOTT.COM</p>
  </main>
</body>
</html>
```